Business Card Design Project

I am community manager and social media strategist. I need a double sided business card with company logo and name. Looking for something professional, elegant but also a little bit original.

• - The logo and the colours are the company colours and a required to stay.
- The size should be: 84 x 55 mm (or 3.30 x 2.16)
- The file size should be: 1039 x 697 pixels (300 dpi)
- I'd like rounded corners. :)

Use the following contact information for the card:

Léonie Vardin
Stratégie médias sociaux / community management / édition de sites sociaux
mob. : 0687529103
leonie.vardin@postelune.fr
Twitter. : @lvardin
Skype : vardin.leonie

```html
<!DOCTYPE html>
<html lang="fr">
<head>
<meta charset="utf-8">
<title>Léonie Vardin — carte de visite</title>
<link rel="stylesheet" href="https://fonts.googleapis.com/css2?family=Open+Sans:wght@400;700&display=swap">
<style>
  :root {
    --ink: #333333;
    --name-blue: #4a8fe6;
    --role-blue: #3568d0;
    --brand-blue: #0b5a91;
    --mark-blue: #0b74ad;
    --divider: #2f68c4;
    --band-light: #5b9ef5;
    --band-dark: #3577d0;
    --lilac-1: #cfd3fa;
    --lilac-2: #9ea2f4;
    --teal-1: #8fd8e8;
    --teal-2: #93a7b0;
    --paper: #ffffff;
  }
  html, body {
    margin: 0;
    padding: 0;
    width: 1200px;
    height: 907px;
    overflow: hidden;
    background: var(--paper);
    font-family: "Open Sans", sans-serif;
  }
  .canvas {
    position: relative;
    width: 1200px;
    height: 907px;
    overflow: hidden;
  }
  .card-back {
    position: absolute;
    left: 0; top: 0;
    width: 594px; height: 907px;
  }
  .card-back svg, .card-front svg { display: block; }
  .back-brand {
    position: absolute;
    left: 505px; top: 440px;
    transform-origin: top left;
    transform: rotate(90deg);
    margin: 0;
    font-weight: 700;
    font-size: 64px;
    letter-spacing: 4px;
    color: var(--brand-blue);
    white-space: nowrap;
  }
  .divider {
    position: absolute;
    left: 635px; top: 0;
    width: 9px; height: 907px;
    background: var(--divider);
  }
  .card-front {
    position: absolute;
    left: 644px; top: 0;
    width: 556px; height: 907px;
  }
  .front-content {
    position: absolute;
    left: 0; top: 0;
    width: 907px; height: 556px;
    transform-origin: top left;
    transform: translate(556px, 0) rotate(90deg);
  }
  .holder-name {
    position: absolute;
    left: 96px; top: 236px;
    margin: 0;
    font-weight: 400;
    font-size: 38px;
    line-height: 1;
    color: var(--name-blue);
    white-space: nowrap;
  }
  .holder-role {
    position: absolute;
    left: 96px; top: 289px;
    margin: 0;
    font-size: 16.5px;
    line-height: 1;
    color: var(--role-blue);
    white-space: nowrap;
  }
  .contact-list {
    position: absolute;
    left: 96px; top: 331px;
    margin: 0;
    padding: 0;
    list-style: none;
    font-size: 20px;
    line-height: 29.5px;
    color: var(--ink);
  }
  .contact-list li { white-space: nowrap; }
  .contact-label { display: inline-block; width: 64px; }
  .front-brand {
    position: absolute;
    left: 660px; top: 383px;
    display: flex;
    flex-direction: column;
    align-items: center;
    gap: 12px;
  }
  .brand-dot {
    width: 96px; height: 96px;
    border-radius: 50%;
    background: var(--mark-blue);
  }
  .brand-name {
    margin: 0;
    font-weight: 700;
    font-size: 42px;
    letter-spacing: 3px;
    line-height: 1;
    color: var(--brand-blue);
  }
</style>
</head>
<body>
<main class="canvas">

  <section class="card-back" aria-label="Verso de la carte">
    <svg width="594" height="907" viewBox="0 0 594 907" aria-hidden="true">
      <defs>
        <linearGradient id="back-tint" x1="0" y1="0" x2="1" y2="1">
          <stop offset="0" stop-color="var(--teal-1)"/>
          <stop offset="0.5" stop-color="var(--teal-2)"/>
          <stop offset="1" stop-color="#9ea4a8"/>
        </linearGradient>
      </defs>
      <rect width="594" height="907" fill="url(#back-tint)"/>
      <path d="M0 10 L440 62 Q594 80 594 160 L594 907 L560 907 L170 850 Q20 830 8 700 L0 640 Z" fill="var(--paper)"/>
      <circle cx="437" cy="227" r="150" fill="var(--mark-blue)"/>
    </svg>
    <p class="back-brand">NAVELIO</p>
  </section>

  <div class="divider"></div>

  <section class="card-front" aria-label="Recto de la carte">
    <svg width="556" height="907" viewBox="0 0 556 907" aria-hidden="true">
      <defs>
        <linearGradient id="front-tint" x1="0" y1="0" x2="0" y2="1">
          <stop offset="0" stop-color="var(--lilac-1)"/>
          <stop offset="0.5" stop-color="var(--lilac-2)"/>
          <stop offset="1" stop-color="var(--lilac-1)"/>
        </linearGradient>
      </defs>
      <rect width="556" height="907" fill="url(#front-tint)"/>
      <ellipse cx="-90" cy="520" rx="648" ry="760" fill="var(--band-light)"/>
      <ellipse cx="-90" cy="520" rx="632" ry="748" fill="var(--band-dark)"/>
      <ellipse cx="-90" cy="520" rx="616" ry="740" fill="var(--paper)"/>
    </svg>

    <div class="front-content">
      <h1 class="holder-name">Léonie Vardin</h1>
      <p class="holder-role">Stratégie médias sociaux / community management / édition de sites sociaux</p>
      <ul class="contact-list">
        <li><span class="contact-label">mob. :</span>0687529103</li>
        <li><span class="contact-label">e-mail:</span>leonie.vardin@postelune.fr</li>
        <li>Twitter : @lvardin</li>
        <li><span class="contact-label">Skype :</span>vardin.leonie</li>
      </ul>
      <div class="front-brand">
        <span class="brand-dot"></span>
        <p class="brand-name">NAVELIO</p>
      </div>
    </div>
  </section>

</main>
</body>
</html>
```